Web Design Project for starting CCTV/Camera security installer/reseller

Hello,

An old class mate is starting his own little CCTV/Camera security business as a one-man-gang.

He asked me to do his website but unfortunatly my design skills are not worth looking at :) The coding is no problem.

So I'm here to request a design.

What he wants is a site that lists the products he might install which is based on a small tree structure. So see it as a shop overview/display but without the baskets & cashout options.

you can find a site structure scheme, logo, product images & data sheet pdf's at this filvaultra address:

https://www.filvaultra.com/sh/kq7zt3908wx4pl2/vnRtLoBe5y/Lumo-Ward

the site itself is http://www.lumo-ward.be but only has a splash screen until I have a design for it.

the logo is a bit out of proportions, not sure if you can make something good out of it :/

Most content is in Dutch, I'll see if I can translate the needed parts...
Updates

Dear designers,

I have some good new for you.

You are allowed to use only that chrome Lumo-Ward part of the logo,
which should make things a lot easier to fit into your design ideas.

Keep up the creativity!

Dear designers,

I uploaded a new logo to the filvaultra space.

It's a png but unfortunately it's not transparent, I'm still waiting for that one
but you know how to erase it in photoshop.

Target Market(s)

people looking for a visual solution to protect their company/home

Industry/Entity Type

Security

Requirements
Must have
• an iconized way to browse/display a tree. (not the traditional folder/explorer style)

maybe first a page with buttons/icons showing level 1 the group types (IP cams, IP servers, Accessories)

level 2 product groups (dome cam, ptz cam etc)

level 3 the actual product + a link to a pdf datasheet (if any)

could be multipage or maybe in/on-page since the product list won't be that huge.

maybe some random product info left and/or right so that the content area is not massive since he has not much to type
;)

```html
<!DOCTYPE html>
<html lang="en">
<head>
<meta charset="utf-8">
<title>Lumo-Ward – CCTV Security Services</title>
<link href="https://fonts.googleapis.com/css2?family=PT+Sans:wght@400;700&family=Yanone+Kaffeesatz:wght@600&family=Questrial&display=swap" rel="stylesheet">
<style>
  :root{
    --blue-dark:#1d4f8c;
    --blue:#2c64a8;
    --blue-text:#1f5a9e;
    --nav-top:#4f86c4;
    --nav-bottom:#23599c;
    --nav-divider:#6d9bd1;
    --ink:#333a44;
    --muted:#555d66;
    --page-bg:#ececec;
    --header-bg:#f4f7fb;
    --white:#ffffff;
    --line:#dfe3e8;
  }
  *{margin:0;padding:0;box-sizing:border-box}
  html,body{width:1056px;height:1200px;overflow:hidden}
  body{
    position:relative;
    background:linear-gradient(#e8e8e8,#e0e0e0 1080px,#ececec);
    font-family:"PT Sans",Arial,sans-serif;color:var(--ink);
  }
  .topline{position:absolute;left:0;top:0;width:1056px;height:5px;background:#d8d8d8}
  .header{position:absolute;left:0;top:5px;width:1056px;height:186px;background:linear-gradient(90deg,#f0f4fa,#ffffff 50%,#f3f6fb)}
  .brand{position:absolute;left:86px;top:52px;display:flex;align-items:center;gap:8px;font-size:21px;color:var(--blue-dark);font-weight:400;letter-spacing:1px}
  .brand-mark{width:14px;height:14px;background:var(--blue)}
  .util-links{position:absolute;right:86px;top:13px;font-size:10px;color:#555}
  .util-links span{margin:0 5px;color:#999}
  .call{position:absolute;right:88px;top:69px;font-size:14px;color:var(--blue-dark)}
  .call strong{font-size:19px;font-weight:400;margin-left:2px}
  .search{position:absolute;left:784px;top:105px;width:195px;height:23px;background:#ebedf0;border:1px solid #e0e3e7;font-size:9.5px;color:#555;padding:5px 9px}
  .search svg{position:absolute;right:7px;top:5px}
  .nav{position:absolute;left:75px;top:143px;width:907px;height:48px;border-radius:4px 4px 0 0;background:linear-gradient(var(--nav-top),var(--nav-bottom));display:flex}
  .nav a{color:var(--white);text-decoration:none;font-size:13.5px;display:flex;align-items:center;justify-content:center;border-right:1px solid var(--nav-divider)}
  .nav a:last-child{border-right:none}
  .page{position:absolute;left:75px;top:191px;width:907px;height:937px;background:var(--white)}
  .hero{position:absolute;left:82px;top:198px;width:890px;height:351px;border:1px solid var(--line);background:linear-gradient(90deg,#fff,#eef3f9)}
  .hero-photo{position:absolute;left:0;top:0;width:620px;height:349px;background:linear-gradient(120deg,#5d8fc7 0%,#a8bfd8 35%,#8a9aa6 60%,#6f8a5e 100%)}
  .hero-copy{position:absolute;left:648px;top:26px;width:220px}
  .hero-copy h1{font-family:"Yanone Kaffeesatz",sans-serif;font-weight:600;font-size:25px;color:var(--blue-dark);margin-bottom:8px}
  .ticks{list-style:none}
  .ticks li{font-size:11.5px;color:var(--blue-text);height:30px;line-height:30px;border-bottom:1px solid #e6ebf1;display:flex;align-items:center;gap:9px;padding-left:4px}
  .ticks li:last-child{border-bottom:none}
  .btn{display:inline-block;background:linear-gradient(#3c76bb,#1f5597);color:var(--white);border-radius:3px;text-decoration:none;font-size:11.5px}
  .hero-copy .btn{margin-top:12px;margin-left:4px;padding:6px 13px}
  .card{position:absolute;top:578px;width:206px}
  .card-img{height:94px;border:1px solid #dcdcdc}
  .card h3{font-size:12.5px;font-weight:700;color:var(--blue-dark);margin:15px 0 4px 4px;font-weight:400}
  .card p{font-size:9.8px;line-height:16px;color:var(--blue-text);margin-left:5px}
  .more{display:block;font-size:11px;color:var(--blue-text);text-decoration:none;margin:7px 0 0 5px}
  .more::after{content:"";display:inline-block;margin-left:6px;border-left:4px solid var(--blue-text);border-top:3px solid transparent;border-bottom:3px solid transparent}
  .divider{position:absolute;left:87px;top:805px;width:879px;height:1px;background:var(--line)}
  .welcome{position:absolute;left:98px;top:829px;width:570px}
  h2{font-family:"Questrial",sans-serif;font-weight:400;font-size:18.5px;color:#222;margin-bottom:9px}
  .welcome h4{font-size:11.5px;font-weight:700;color:#333;margin-bottom:6px}
  .welcome p{font-size:11px;line-height:19.5px;color:var(--muted)}
  .welcome p.gap{margin-top:3px}
  .why{position:absolute;left:693px;top:829px;width:270px}
  .why-img{width:265px;height:108px;background:linear-gradient(100deg,#c9a386,#6b5a48 30%,#d0a96a 60%,#8e7e55)}
  .why h5{font-family:"Questrial",sans-serif;font-weight:400;font-size:13.5px;color:#333;margin:9px 0 6px}
  .why p{font-size:10.5px;line-height:19.5px;color:var(--muted)}
  .why .btn{margin-top:10px;padding:5px 12px;font-size:10px}
  .footer{position:absolute;left:87px;top:1146px;width:891px;font-size:9.5px;color:#555;display:flex;justify-content:space-between}
  .footer nav a{color:#555;text-decoration:none;margin-left:16px}
</style>
</head>
<body>
  <div class="topline"></div>
  <header class="header"></header>

  <div class="brand"><span class="brand-mark"></span>Lumo-Ward</div>
  <div class="util-links">Support<span>|</span>FAQ<span>|</span>Hire Us<span>|</span>Sitemap</div>
  <div class="call">Call Us Now <strong>555-214-7730</strong></div>
  <div class="search">Enter keyword
    <svg width="13" height="13" viewBox="0 0 13 13"><circle cx="5.5" cy="5.5" r="4" fill="none" stroke="#777" stroke-width="1.6"/><line x1="8.5" y1="8.5" x2="12" y2="12" stroke="#777" stroke-width="1.8"/></svg>
  </div>

  <nav class="nav">
    <a href="#" style="width:96px">Home</a>
    <a href="#" style="width:110px">About Us</a>
    <a href="#" style="width:133px">Why Choose Us</a>
    <a href="#" style="width:166px">Cameras &amp; Sercurity</a>
    <a href="#" style="width:86px">Review</a>
    <a href="#" style="width:122px">Testimonials</a>
    <a href="#" style="width:115px">Recent Blog</a>
    <a href="#" style="width:79px">Contact</a>
  </nav>

  <main class="page"></main>

  <section class="hero">
    <div class="hero-photo" role="img" aria-label="Operator on the phone pointing at a wall of security monitors"></div>
    <div class="hero-copy">
      <h1>CCTV Security Services</h1>
      <ul class="ticks">
        <li><svg width="10" height="9" viewBox="0 0 10 9"><path d="M1 5l3 3 5-7" fill="none" stroke="#1d4f8c" stroke-width="2"/></svg>Duis tincidunt lectus quis dui viverra.</li>
        <li><svg width="10" height="9" viewBox="0 0 10 9"><path d="M1 5l3 3 5-7" fill="none" stroke="#1d4f8c" stroke-width="2"/></svg>Suspendisse vulputate aliquam dui.</li>
        <li><svg width="10" height="9" viewBox="0 0 10 9"><path d="M1 5l3 3 5-7" fill="none" stroke="#1d4f8c" stroke-width="2"/></svg>Nulla elementum dui ut augue.</li>
        <li><svg width="10" height="9" viewBox="0 0 10 9"><path d="M1 5l3 3 5-7" fill="none" stroke="#1d4f8c" stroke-width="2"/></svg>Aliquam vehicula mi at mauris.</li>
        <li><svg width="10" height="9" viewBox="0 0 10 9"><path d="M1 5l3 3 5-7" fill="none" stroke="#1d4f8c" stroke-width="2"/></svg>Maecenas placerat.</li>
        <li><svg width="10" height="9" viewBox="0 0 10 9"><path d="M1 5l3 3 5-7" fill="none" stroke="#1d4f8c" stroke-width="2"/></svg>Nisl at consequat rhoncus.</li>
        <li><svg width="10" height="9" viewBox="0 0 10 9"><path d="M1 5l3 3 5-7" fill="none" stroke="#1d4f8c" stroke-width="2"/></svg>Quis eleifend arcu velit quis lacus.</li>
      </ul>
      <a href="#" class="btn">Learn More</a>
    </div>
  </section>

  <article class="card" style="left:87px">
    <div class="card-img" role="img" aria-label="Assorted CCTV cameras" style="background:linear-gradient(#f6f6f6,#d9dadc)"></div>
    <h3>CCCTV Camera</h3>
    <p>Praesent vitae lacus. Ut velit enim, vestibu-lum non, fermentum nec, hendrerit quis, leo. Pellentesque rutrum malesuada neque.</p>
    <a href="#" class="more">Learn More</a>
  </article>
  <article class="card" style="left:314px">
    <div class="card-img" role="img" aria-label="Monitoring room with operators at screens" style="background:linear-gradient(160deg,#3d5fa8,#8b8f9a 55%,#4a4d55)"></div>
    <h3>CCCTV Monitoring</h3>
    <p>Praesent vitae lacus. Ut velit enim, vestibu-lum non, fermentum nec, hendrerit quis, leo. Pellentesque rutrum malesuada neque.</p>
    <a href="#" class="more">Learn More</a>
  </article>
  <article class="card" style="left:540px">
    <div class="card-img" role="img" aria-label="Security cameras on a pole against blue sky" style="background:linear-gradient(#6ea4dd,#8fbbe6)"></div>
    <h3 style="margin-top:17px">Cam Security</h3>
    <p>Praesent vitae lacus. Ut velit enim, vestibu-lum non, fermentum nec, hendrerit quis, leo. Pellentesque rutrum malesuada neque.</p>
    <a href="#" class="more">Learn More</a>
  </article>
  <article class="card" style="left:762px">
    <div class="card-img" role="img" aria-label="Video storage server beside a laptop" style="background:linear-gradient(90deg,#9a9a9a,#cfcfcf 50%,#5b8cc9)"></div>
    <h3 style="margin-top:17px">Video Storage Systems</h3>
    <p>Praesent vitae lacus. Ut velit enim, vestibu-lum non, fermentum nec, hendrerit quis, leo. Pellentesque rutrum malesuada neque.</p>
    <a href="#" class="more">Learn More</a>
  </article>

  <div class="divider"></div>

  <section class="welcome">
    <h2>Welcome to Our Website Mainpage</h2>
    <h4>Are you looking for a camera system for your home or company?</h4>
    <p>Then you are at Lumo-Ward at the right address!<br>
    We offer a large amount of surveilance camera's, video storage systems and surveilance monitors.<br>
    But we also have complete camera surveillance sets for you (analogue or IP camera's) including the cables and power supplies, so that you don't have to worry about additional components when ordering</p>
    <p class="gap">Suspendisse quam leo, molestie sed, luctus quis, feugiat in, pede. Fusce tellus. Sed metus augue, convallis et, vehicula ut, pulvinar eu, ante. Integer orci tellus, tristique vitae, consequat nec, porta vel, lectus. Nulla sit amet diam. Duis non nunc. Nulla rhoncus dictum metus. Curabitur tristique mi condimentum orci.<br>
    Phasellus pellentesque aliquam enim. Proin dui lectus, cursus eu, mattis laoreet, viverra sit amet, quam. Curabitur vel dolor ultrices ipsum dictum tristique. Praesent vitae lacus. Ut velit enim, vestibulum non, fermentum nec, hendrerit quis, leo. Pellentesque rutrum malesuada neque.</p>
  </section>

  <aside class="why">
    <h2>Why Choose Us</h2>
    <div class="why-img" role="img" aria-label="Security guard watching a bank of monitors"></div>
    <h5>Nulla rhoncus dictum metus.</h5>
    <p>Curabitur tristique mi condimentum orci. Phasellus pellentesque aliquam enim. Proin dui lectus, cursus eu, mattis laoreet, viverra sit amet, quam.</p>
    <a href="#" class="btn">Learn More</a>
  </aside>

  <footer class="footer">
    <span>© 2012 Company Name.&nbsp; All right reserved.&nbsp; Term of Use</span>
    <nav><a href="#">Home</a><a href="#">About Us</a><a href="#">Why Choose Us</a><a href="#">Cameras &amp; Sercurity</a><a href="#">Review</a><a href="#">Testimonials</a><a href="#">Contact</a></nav>
  </footer>
</body>
</html>
```